I am looking for a Business Card Design for my spirit company titled "Harbor Pour Co" The company specializes in prohibition style/speakeasy mixology drinks and alcohol distribution. I am looking for Retro, Masculine, Sophisticated Card that embodies the look of Prohibition. Black and White colors. Also add Facebook, Instgram logo

Information that should go on the card is my Name, Title, Phone, Email, Website as follows:

Tobias K Verran
Principal
301.555.0187
tobias@harborpourco.example
harborpourco.example
Updates

Hello all I have uploaded a pdf version of the logo. It seems as if some are saying the resolution is too small.

Target Market(s)

Male and Female drinkers of all ages with a sophisticated palate that have an appreciation for fine crafted cocktail

Industry/Entity Type

Business

Requirements
Must have
• Information that should go on the card is my Name, Title, Phone, Email, Website as follows:

Tobias K Verran
Principal
301.555.0187
tobias@harborpourco.example
harborpourco.example

```html
<!DOCTYPE html>
<html lang="en">
<head>
<meta charset="utf-8">
<title>Harbor Pour Co — Business Card</title>
<link rel="stylesheet" href="https://fonts.googleapis.com/css2?family=Open+Sans:wght@400;600;700&display=swap">
<style>
  :root {
    --backdrop: #3a3330;
    --card: #141414;
    --card-edge: #242424;
    --ink: #f2f2f2;
    --ink-soft: #cfcfcf;
    --ink-muted: #9a9a9a;
    --ink-gloss: #8c8c8c;
    --rule: #5a5a5a;
  }
  * { box-sizing: border-box; margin: 0; padding: 0; }
  html, body {
    width: 1200px; height: 788px; overflow: hidden;
    background: var(--backdrop);
    font-family: "Open Sans", Arial, sans-serif;
  }
  .stage {
    width: 1200px; height: 788px;
    display: flex; align-items: center; justify-content: center; gap: 40px;
  }
  .card {
    width: 540px; height: 310px;
    background: var(--card);
    border: 1px solid var(--card-edge);
    border-radius: 3px;
    position: relative;
    color: var(--ink);
  }

  /* Brand: name set inside one plain ring */
  .brand {
    border-radius: 50%;
    border: 3px solid var(--ink);
    display: flex; align-items: center; justify-content: center;
    text-align: center;
  }
  .brand__name {
    font-weight: 600;
    text-transform: uppercase;
    letter-spacing: 3px;
    line-height: 1.25;
    color: var(--ink);
  }

  /* Front */
  .card--front { display: flex; align-items: center; justify-content: center; }
  .card--front .brand { width: 190px; height: 190px; border-color: var(--ink-gloss); }
  .card--front .brand__name { font-size: 22px; color: var(--ink-gloss); }

  /* Back */
  .card--back .brand {
    position: absolute; left: 52px; top: 80px;
    width: 150px; height: 150px;
  }
  .card--back .brand__name { font-size: 17px; }
  .divider {
    position: absolute; left: 238px; top: 110px;
    width: 1px; height: 110px; background: var(--rule);
  }
  .identity { position: absolute; left: 268px; top: 64px; }
  .identity__name { font-weight: 700; font-size: 22px; color: var(--ink); line-height: 1.2; }
  .identity__title { font-size: 13px; color: var(--ink-muted); }
  .contacts {
    position: absolute; left: 258px; top: 178px;
    list-style: none; font-size: 14px; color: var(--ink-soft);
  }
  .contacts li { display: flex; align-items: center; gap: 10px; height: 21px; }
  .contacts svg { width: 12px; height: 12px; fill: var(--ink-soft); flex: none; }
  .social-mark { width: 12px; height: 12px; background: var(--ink-soft); border-radius: 2px; flex: none; }
</style>
</head>
<body>
<main class="stage">
  <section class="card card--front" aria-label="Card front">
    <div class="brand">
      <span class="brand__name">Harbor<br>Pour Co</span>
    </div>
  </section>

  <section class="card card--back" aria-label="Card back">
    <div class="brand">
      <span class="brand__name">Harbor<br>Pour Co</span>
    </div>
    <div class="divider"></div>
    <div class="identity">
      <p class="identity__name">Tobias K Verran</p>
      <p class="identity__title">Principal</p>
    </div>
    <ul class="contacts">
      <li>
        <svg viewBox="0 0 24 24"><path d="M6.6 10.8a15.1 15.1 0 0 0 6.6 6.6l2.2-2.2c.3-.3.7-.4 1-.2 1.1.4 2.3.6 3.6.6.6 0 1 .4 1 1V20c0 .6-.4 1-1 1A17 17 0 0 1 3 4c0-.6.4-1 1-1h3.5c.6 0 1 .4 1 1 0 1.3.2 2.5.6 3.6.1.3 0 .7-.2 1z"/></svg>
        301.555.0187
      </li>
      <li>
        <svg viewBox="0 0 24 24"><path d="M2 5h20v14H2z M2 5l10 8 10-8" fill="none" stroke="#cfcfcf" stroke-width="2.4"/></svg>
        tobias@harborpourco.example
      </li>
      <li>
        <svg viewBox="0 0 24 24"><circle cx="12" cy="12" r="9" fill="none" stroke="#cfcfcf" stroke-width="2.4"/><path d="M3 12h18M12 3c3 3 3 15 0 18M12 3c-3 3-3 15 0 18" fill="none" stroke="#cfcfcf" stroke-width="2"/></svg>
        www.harborpourco.example
      </li>
      <li>
        <span class="social-mark" aria-hidden="true"></span>
        harborpourco.example
      </li>
    </ul>
  </section>
</main>
</body>
</html>
```